Corvane Supplies Business Card

Professional business card that stand out to our potential customers. Front and back with clean modern design

Industry/Entity Type

Oil and gas

Contact Information for Business Card

Name, address, website , office phone and cell number

Requirements
Must have
• Editable files for each employee

```html
<!DOCTYPE html>
<html lang="en">
<head>
<meta charset="utf-8">
<title>Corvane Supplies Business Card</title>
<link rel="stylesheet" href="https://fonts.googleapis.com/css2?family=Montserrat:wght@400;500;600;700&display=swap">
<style>
  :root {
    --brand-red: #ed1c24;
    --brand-cyan: #10b1d3;
    --ink: #231f20;
    --card-white: #ffffff;
    --card-dark: #231f20;
    --backdrop: #3a3a3c;
  }
  * { margin: 0; padding: 0; box-sizing: border-box; }
  html, body {
    width: 1200px;
    height: 1059px;
    overflow: hidden;
    background: var(--backdrop);
    font-family: "Montserrat", sans-serif;
  }
  .canvas { position: relative; width: 1200px; height: 1059px; }

  .card {
    position: absolute;
    width: 690px;
    height: 393px;
    box-shadow: 0 14px 28px rgba(0,0,0,.55);
  }
  .card-front { left: 256px; top: 100px; background: var(--card-white); }
  .card-back { left: 254px; top: 537px; background: var(--card-dark); }

  .accent-tab {
    position: absolute;
    left: 0; top: 190px;
    width: 15px; height: 46px;
    background: var(--brand-red);
    border-radius: 0 5px 5px 0;
  }
  .person-name {
    position: absolute;
    left: 27px; top: 183px;
    font-size: 29px;
    font-weight: 700;
    letter-spacing: .3px;
    color: var(--brand-red);
  }
  .person-name .surname { color: var(--brand-cyan); }
  .person-role {
    position: absolute;
    left: 28px; top: 221px;
    font-size: 15px;
    font-weight: 400;
    letter-spacing: .6px;
    color: var(--ink);
  }
  .divider {
    position: absolute;
    left: 28px; top: 256px;
    width: 638px; height: 2px;
    background: var(--brand-cyan);
  }
  .contact-list {
    position: absolute;
    left: 28px; top: 273px;
    list-style: none;
  }
  .contact-list li {
    display: flex;
    align-items: center;
    height: 23.5px;
    font-size: 15.5px;
    letter-spacing: .6px;
    color: var(--ink);
  }
  .contact-list svg { width: 13px; height: 13px; margin-right: 8px; flex: none; }
  .location {
    position: absolute;
    right: 22px; top: 343px;
    display: flex; align-items: center;
    font-size: 15.5px;
    letter-spacing: .6px;
    color: var(--ink);
  }
  .location svg { width: 12px; height: 16px; margin-left: 9px; }

  .brand-front {
    position: absolute;
    right: 24px; top: 168px;
    display: flex; align-items: center;
  }
  .brand-mark {
    width: 18px; height: 18px;
    background: var(--brand-cyan);
    margin-right: 10px;
  }
  .brand-name {
    font-size: 22px;
    font-weight: 700;
    letter-spacing: .5px;
    color: var(--brand-red);
  }

  .brand-back {
    position: absolute;
    left: 0; right: 0; top: 0; bottom: 0;
    display: flex; align-items: center; justify-content: center;
  }
  .brand-back .brand-mark { width: 30px; height: 30px; margin-right: 16px; }
  .brand-back .brand-name { font-size: 38px; }
</style>
</head>
<body>
<div class="canvas">

  <section class="card card-front">
    <div class="brand-front">
      <span class="brand-mark"></span>
      <span class="brand-name">Corvane Supplies</span>
    </div>

    <span class="accent-tab"></span>
    <h1 class="person-name">Daniel <span class="surname">Marsh</span></h1>
    <p class="person-role">Manager</p>
    <div class="divider"></div>

    <ul class="contact-list">
      <li>
        <svg viewBox="0 0 16 16" aria-hidden="true"><path fill="var(--brand-red)" d="M3.6 1.5l2.3 2.6-1.2 1.6c.8 1.9 2.3 3.4 4.2 4.3l1.6-1.2 2.6 2.3-1.5 2.4C6.5 13.6 2.3 9.4 1.3 4.3z"/><path fill="none" stroke="var(--brand-red)" stroke-width="1.3" d="M9 2.5a4.5 4.5 0 0 1 4.5 4.5M9 5a2 2 0 0 1 2 2"/></svg>
        1-555-010-0142
      </li>
      <li>
        <svg viewBox="0 0 16 16" aria-hidden="true"><rect x="1" y="3" width="14" height="10" rx="1" fill="var(--brand-red)"/><path d="M1.5 4l6.5 5 6.5-5" fill="none" stroke="#fff" stroke-width="1.2"/></svg>
        dmarsh@kestrelparts.vn
      </li>
      <li>
        <svg viewBox="0 0 16 16" aria-hidden="true"><g fill="none" stroke="var(--brand-red)" stroke-width="1.3"><circle cx="8" cy="8" r="6.5"/><ellipse cx="8" cy="8" rx="3" ry="6.5"/><path d="M1.5 8h13M2.5 4.8h11M2.5 11.2h11"/></g></svg>
        www.kestrelparts.vn
      </li>
      <li>
        <svg viewBox="0 0 16 16" aria-hidden="true"><g fill="none" stroke="var(--brand-red)" stroke-width="1.3"><circle cx="8" cy="8" r="6.5"/><ellipse cx="8" cy="8" rx="3" ry="6.5"/><path d="M1.5 8h13M2.5 4.8h11M2.5 11.2h11"/></g></svg>
        www.kestrelparts.com
      </li>
    </ul>

    <p class="location">
      Ho Chi Minh, Vietnam
      <svg viewBox="0 0 12 16" aria-hidden="true"><path fill="var(--brand-red)" d="M6 0a6 6 0 0 0-6 6c0 4.2 6 10 6 10s6-5.8 6-10a6 6 0 0 0-6-6zm0 8.5A2.5 2.5 0 1 1 6 3.5a2.5 2.5 0 0 1 0 5z"/></svg>
    </p>
  </section>

  <section class="card card-back">
    <div class="brand-back">
      <span class="brand-mark"></span>
      <span class="brand-name">Corvane Supplies</span>
    </div>
  </section>

</div>
</body>
</html>
```